Redesign of WordHarbor.com in Bootstrap 4

Current design of WordHarbor.com is not responsive. We need to change it to latest version of Bootstrap 4 keeping essential elements in place.

Apart from home page, we need designs for http://www.wordharbor.com/meaning/cat also.

Coding

Coded - Design and coding required

Number of Pages Required

2 page

Colors
34a7d8

Requirements
Must have
• Bootstrap 4

```html
<!DOCTYPE html>
<html lang="en">
<head>
<meta charset="utf-8">
<title>Cat meaning – WordHarbor.com</title>
<link rel="stylesheet" href="https://fonts.googleapis.com/css2?family=Roboto:wght@400;500&family=Oswald:wght@300;400&display=swap">
<style>
:root{
  --brand:#34a7d8;
  --ink:#222;
  --card-bg:#fafafa;
  --card-line:#ebebeb;
  --footer-bg:#21222b;
  --footer-text:#e6e6e6;
  --muted:#8a8a90;
  --cell-a:#ffffff;
  --cell-b:#e0e0e0;
  --cell-text:#666;
}
*{box-sizing:border-box;margin:0;padding:0}
html,body{width:1200px;height:1059px;overflow:hidden;background:#fff;font-family:'Roboto',sans-serif}
.page{position:relative;width:1200px;height:1059px}
.results{position:absolute;left:131px;top:-72px;width:938px}
.entry{height:76px;margin-bottom:2.4px;background:var(--card-bg);border:1px solid var(--card-line);padding:0 12px;position:relative}
.entry-word{position:absolute;left:12px;top:19px;display:flex;align-items:center;gap:8px;color:var(--brand);font-size:16px;font-weight:500;line-height:20px}
.entry-word svg{width:17px;height:17px}
.entry-def{position:absolute;left:12px;top:46px;font-size:12px;font-weight:500;color:var(--ink);line-height:16px}
.browse{position:absolute;left:0;top:546px;width:1200px;height:136px;background:var(--brand);text-align:center}
.browse-title{font-family:'Oswald',sans-serif;font-weight:400;font-size:37px;color:#fff;line-height:1;margin-top:27px;letter-spacing:-.3px}
.alphabet{display:flex;justify-content:center;margin-top:22px;list-style:none}
.alphabet li{width:28.8px;height:29px;line-height:29px;font-size:18px;color:var(--cell-text);background:var(--cell-a)}
.alphabet li:nth-child(even){background:var(--cell-b)}
.site-footer{position:absolute;left:0;top:682px;width:1200px;height:377px;background:var(--footer-bg)}
.footer-col{position:absolute;top:34px}
.footer-heading{color:var(--brand);font-size:16px;font-weight:500;line-height:20px;position:relative;padding-bottom:6px}
.footer-heading::after{content:"";position:absolute;left:0;bottom:0;width:13px;height:2px;background:var(--brand)}
.footer-links{list-style:none;margin-top:15px}
.footer-links li{font-size:12px;font-weight:500;color:var(--footer-text);line-height:20.8px}
.subscribe-input{position:absolute;left:869px;top:80px;width:200px;height:40px;border:1px dashed #3a3b44;background:var(--footer-bg);color:#888;font-size:12px;padding-left:11px;line-height:38px}
.subscribe-btn{position:absolute;left:869px;top:132px;width:200px;height:27px;background:var(--brand);border:1px solid #5bbbe3;color:#fff;font-family:'Oswald',sans-serif;font-size:16px;line-height:25px;text-align:center}
.tagline{position:absolute;left:0;top:206px;width:1200px;text-align:center;font-family:'Oswald',sans-serif;font-weight:300;font-size:22px;color:var(--footer-text)}
.copyright{position:absolute;left:0;top:261px;width:1200px;text-align:center;font-size:10px;color:var(--muted)}
</style>
</head>
<body>
<div class="page">
  <section class="results">
    <article class="entry"></article>
    <article class="entry"><div class="entry-word">Cat <svg viewBox="0 0 20 20"><circle cx="10" cy="10" r="8.8" fill="none" stroke="#34a7d8" stroke-width="1.6"/><path d="M8 6l6 4-6 4z" fill="#34a7d8"/></svg></div><p class="entry-def">/ˈkæt/ ? &nbsp;feline mammal usually having thick soft fur and no ability to roar: domestic cats;...</p></article>
    <article class="entry"><div class="entry-word">Cat <svg viewBox="0 0 20 20"><circle cx="10" cy="10" r="8.8" fill="none" stroke="#34a7d8" stroke-width="1.6"/><path d="M8 6l6 4-6 4z" fill="#34a7d8"/></svg></div><p class="entry-def">/ˈkæt/ ? &nbsp;feline mammal usually having thick soft fur and no ability to roar: domestic cats;...</p></article>
    <article class="entry"><div class="entry-word">Cat <svg viewBox="0 0 20 20"><circle cx="10" cy="10" r="8.8" fill="none" stroke="#34a7d8" stroke-width="1.6"/><path d="M8 6l6 4-6 4z" fill="#34a7d8"/></svg></div><p class="entry-def">/ˈkæt/ ? &nbsp;feline mammal usually having thick soft fur and no ability to roar: domestic cats;...</p></article>
    <article class="entry"><div class="entry-word">Cat <svg viewBox="0 0 20 20"><circle cx="10" cy="10" r="8.8" fill="none" stroke="#34a7d8" stroke-width="1.6"/><path d="M8 6l6 4-6 4z" fill="#34a7d8"/></svg></div><p class="entry-def">/ˈkæt/ ? &nbsp;feline mammal usually having thick soft fur and no ability to roar: domestic cats;...</p></article>
    <article class="entry"><div class="entry-word">Cat <svg viewBox="0 0 20 20"><circle cx="10" cy="10" r="8.8" fill="none" stroke="#34a7d8" stroke-width="1.6"/><path d="M8 6l6 4-6 4z" fill="#34a7d8"/></svg></div><p class="entry-def">/ˈkæt/ ? &nbsp;feline mammal usually having thick soft fur and no ability to roar: domestic cats;...</p></article>
    <article class="entry"><div class="entry-word">Cat <svg viewBox="0 0 20 20"><circle cx="10" cy="10" r="8.8" fill="none" stroke="#34a7d8" stroke-width="1.6"/><path d="M8 6l6 4-6 4z" fill="#34a7d8"/></svg></div><p class="entry-def">/ˈkæt/ ? &nbsp;feline mammal usually having thick soft fur and no ability to roar: domestic cats;...</p></article>
  </section>

  <section class="browse">
    <h2 class="browse-title">Browse Dictionary</h2>
    <ul class="alphabet">
      <li>A</li><li>B</li><li>C</li><li>D</li><li>E</li><li>F</li><li>G</li><li>H</li><li>I</li><li>J</li><li>K</li><li>L</li><li>M</li><li>N</li><li>O</li><li>P</li><li>Q</li><li>R</li><li>S</li><li>T</li><li>U</li><li>V</li><li>W</li><li>X</li><li>Y</li><li>Z</li>
    </ul>
  </section>

  <footer class="site-footer">
    <div class="footer-col" style="left:142px"><h3 class="footer-heading">Sitemap</h3><ul class="footer-links"><li>FAQ</li><li>Contact</li><li>Blog</li></ul></div>
    <div class="footer-col" style="left:377px"><h3 class="footer-heading">Legal</h3><ul class="footer-links"><li>Privacy Policy</li><li>Terms of Use</li></ul></div>
    <div class="footer-col" style="left:625px"><h3 class="footer-heading">Others</h3><ul class="footer-links"><li>Popular Words</li><li>Common Errors in English</li><li>Exam Prep Online</li></ul></div>
    <div class="footer-col" style="left:870px"><h3 class="footer-heading">Subscribe</h3></div>
    <div class="subscribe-input">Email Id</div>
    <div class="subscribe-btn">SUBMIT</div>
    <p class="tagline">Meaning/Definition, Audio, Phonetics, Usages and more</p>
    <p class="copyright">© 2016. @ WORDHARBOR. All Rights Reserved.</p>
  </footer>
</div>
</body>
</html>
```